QM Interiors needs and Interior Design Business card

I can do anything from Commercial to Residential and Free lance. Beginning to end in design selection process.
Need something to catch the eye of potential customers and vendors. From furniture to Tile and Cabinet selections. I can do it all.

Industry/Entity Type

Design Agency

Contact Information for Business Card

QM Interiors- Design Consultanting Residential, Commerical
Maybe a cool detail background. Wall paper print that can have some texture

Font styles to use
Serif

Colors
709dcb
34a6d7
b868aa
e667a6
f59296
85acd3
ffffff
000000
5c5c5c

Requirements
Must have
• Square or Rectangular with Rounded edges
• Name
• Address
• Phone
• Email
Nice to have
• Some colored edges More simples not too busy
• Pattern detail in background.
Should not have
• Not too much color

```html
<!DOCTYPE html>
<html lang="en">
<head>
<meta charset="utf-8">
<title>QM Interiors – Business Card</title>
<link rel="stylesheet" href="https://fonts.googleapis.com/css2?family=Didact+Gothic&family=Open+Sans:wght@400;700;800&display=swap">
<style>
  :root {
    --stage: #2b2b2b;
    --ink: #000000;
    --paper: #ffffff;
    --accent-blue: #34a6d7;
    --soft-blue: #85acd3;
    --text-light: #ffffff;
  }
  * { box-sizing: border-box; margin: 0; padding: 0; }
  html, body { width: 1200px; height: 900px; overflow: hidden; }
  body { background: var(--stage); position: relative; font-family: "Open Sans", sans-serif; }

  .card {
    position: absolute;
    width: 600px;
    height: 345px;
    border-radius: 8px;
    overflow: hidden;
  }

  /* Back side */
  .card-back { left: 90px; top: 70px; background: var(--ink); }
  .back-mark {
    position: absolute; left: 50%; top: 50%;
    width: 190px; height: 190px; margin: -95px 0 0 -95px;
    border: 6px solid var(--soft-blue); border-radius: 50%;
    display: flex; align-items: center; justify-content: center;
  }
  .back-name {
    font-family: "Didact Gothic", sans-serif;
    color: var(--soft-blue); font-size: 22px; letter-spacing: 0.08em;
  }

  /* Front side */
  .card-front { left: 510px; top: 470px; background: var(--paper); }
  .brand-title {
    position: absolute; left: 0; right: 0; top: 62px;
    text-align: center; padding-right: 40px;
    font-family: "Didact Gothic", sans-serif;
    font-size: 46px; letter-spacing: 0.22em; color: var(--ink);
  }
  .rule { position: absolute; left: 0; width: 100%; height: 3px; background: var(--accent-blue); }
  .rule-top { top: 160px; }
  .rule-bottom { top: 304px; }
  .band { position: absolute; left: 0; top: 168px; width: 100%; height: 130px; background: var(--ink); }

  .front-mark {
    position: absolute; right: 18px; top: 100px;
    width: 130px; height: 130px;
    background: var(--paper); border: 6px solid var(--ink); border-radius: 50%;
    display: flex; align-items: center; justify-content: center;
  }
  .front-mark-name { font-family: "Didact Gothic", sans-serif; font-size: 15px; letter-spacing: 0.05em; color: var(--ink); }

  .contact { position: absolute; left: 34px; top: 178px; color: var(--text-light); }
  .person-name { font-weight: 800; font-size: 22px; line-height: 1.1; letter-spacing: 0.01em; }
  .person-role { color: var(--accent-blue); font-size: 12px; letter-spacing: 0.05em; margin-bottom: 3px; }
  .contact-line { font-size: 13px; line-height: 1.35; display: flex; align-items: center; gap: 6px; }
  .contact-line svg { width: 10px; height: 10px; fill: var(--accent-blue); flex: none; }
  .indent { padding-left: 16px; }
</style>
</head>
<body>

  <div class="card card-back">
    <div class="back-mark"><span class="back-name">QM Interiors</span></div>
  </div>

  <div class="card card-front">
    <div class="brand-title">QM Interiors</div>
    <div class="rule rule-top"></div>
    <div class="band"></div>
    <div class="rule rule-bottom"></div>

    <div class="front-mark"><span class="front-mark-name">QM Interiors</span></div>

    <div class="contact">
      <div class="person-name">DANA WHITLOW</div>
      <div class="person-role">DIRECTOR</div>
      <div class="contact-line indent">Unit 2/9 Harbour Lane</div>
      <div class="contact-line indent">MILTON, QLD 4064</div>
      <div class="contact-line">
        <svg viewBox="0 0 10 10" aria-hidden="true"><path d="M2 0.5 L3.6 0.5 L4.2 2.8 L3 3.6 Q4 5.8 6.4 7 L7.2 5.8 L9.5 6.4 L9.5 8 Q9.5 9.5 8 9.5 Q0.5 9 0.5 2 Q0.5 0.5 2 0.5 Z"/></svg>
        +330 2175-0394
      </div>
      <div class="contact-line">
        <svg viewBox="0 0 10 10" aria-hidden="true"><path d="M0.5 2 H9.5 V8.5 H0.5 Z M1.4 2.8 V7.7 H8.6 V2.8 L5 5.4 Z" fill-rule="evenodd"/></svg>
        info@qminteriors.com
      </div>
    </div>
  </div>

</body>
</html>
```